Looking for a website design for my company
Services we offer:
Phone Repair
TV Mounting
Security Camera Installation
Networking / Wi-Fi
Smart Home Services
IT Support

Looking for a website similar to qarnel.com

Few tabs
About Us
Contact Us
Areas Served
Pricing and Services

```html
<!DOCTYPE html>
<html lang="en">
<head>
<meta charset="utf-8">
<title>Vanto Rim – Home Tech Services</title>
<link href="https://fonts.googleapis.com/css2?family=Poppins:ital,wght@0,400;0,500;0,600;0,700;1,400&display=swap" rel="stylesheet">
<style>
:root{
  --orange:#f7931e;
  --orange-dark:#e8800c;
  --ink:#222;
  --text:#555;
  --muted:#777;
  --light:#f4f4f4;
  --dark:#262626;
  --darker:#1d1d1d;
  --blue:#1d6cf0;
  --sky:#23b7f2;
  --white:#fff;
}
*{box-sizing:border-box;margin:0;padding:0}
html,body{width:1200px;height:3013px;overflow:hidden}
body{font-family:'Poppins',sans-serif;color:var(--text);background:var(--white);position:relative}
.abs{position:absolute}
.brand{font-family:'Poppins',sans-serif;font-weight:700;color:var(--orange);letter-spacing:-.5px}
.btn{display:inline-flex;align-items:center;justify-content:center;background:var(--orange);color:#fff;font-weight:600;font-size:12px;border-radius:4px;text-transform:uppercase;letter-spacing:.3px}

/* header */
.site-header{position:absolute;top:0;left:0;width:1200px;height:63px;background:#fff;border-bottom:1px solid #eee}
.site-header .brand{left:150px;top:10px;font-size:34px}
.main-nav{left:346px;top:24px;display:flex;gap:32px;font-size:12px;color:#333}
.phone-pill{left:897px;top:19px;width:154px;height:29px;border:1px solid var(--orange);border-radius:15px;display:flex;align-items:center;gap:6px;padding-left:9px;font-size:12.5px;color:#333}
.phone-pill .ico{width:16px;height:16px;border-radius:50%;background:var(--orange);display:flex;align-items:center;justify-content:center}

/* hero */
.hero{top:63px;left:0;width:1200px;height:431px;background:linear-gradient(90deg,#e8e7e3 0%,#d9d6cf 35%,#7d8a9b 60%,#2b3a6e 70%,#c7cbd2 88%,#aeb6c0 100%)}
.hero h1{left:147px;top:170px;font-size:28px;line-height:33px;font-weight:700;color:#222}
.hero p{left:147px;top:240px;width:305px;font-size:10.5px;line-height:16px;color:#333}
.hero .btn{left:150px;top:292px;width:130px;height:36px}
.dots{left:567px;top:407px;display:flex;gap:4px}
.dots i{display:block;width:20px;height:3px;background:#fff}
.dots i:nth-child(2){background:#ccd}

/* about */
.about{top:494px;left:0;width:1200px;height:408px;background:linear-gradient(90deg,#fff 55%,#f2f3f5 100%)}
.about h2{left:149px;top:85px;font-size:27px;font-weight:500;color:#222}
.about h2 .brand{font-size:27px}
.about .copy{left:149px;top:130px;width:422px;font-size:10.5px;line-height:19.5px;color:#555;text-align:justify}
.about .copy p+p{margin-top:19px}
.about-img-a{left:683px;top:68px;width:226px;height:242px;background:linear-gradient(135deg,#f7a234,#e9861a)}
.about-img-b{left:802px;top:105px;width:249px;height:243px;background:radial-gradient(circle at 50% 50%,#2a6a86,#0d2f45 75%)}

/* services */
.services{top:902px;left:0;width:1200px;height:640px;background:var(--light)}
.services h2{left:0;width:1200px;top:55px;text-align:center;font-size:28px;font-weight:500;color:#333}
.card{position:absolute;width:294px;height:223px;background:#fff;border:1px solid #e2e2e2}
.card .pic{height:185px}
.card .label{height:38px;display:flex;align-items:center;justify-content:space-between;padding-left:14px;font-size:15px;font-weight:600;color:#222}
.card .go{width:34px;height:38px;background:var(--orange);display:flex;align-items:center;justify-content:center}

/* simple way */
.simple{top:1542px;left:0;width:1200px;height:267px;background:#fff;border-top:1px solid #e6e6e6;border-bottom:1px solid #e6e6e6}
.simple h2{left:150px;top:35px;width:360px;font-size:27px;line-height:33px;font-weight:500;color:#222}
.simple p{left:150px;top:110px;width:355px;font-size:10.5px;line-height:16.5px;color:#777}
.simple .btn{left:151px;top:192px;width:130px;height:36px}
.simple .photo{left:575px;top:0;width:625px;height:266px;background:linear-gradient(90deg,#c9c3b7,#e6e1d8 40%,#d7cdbf 70%,#b9b4ab)}

/* areas + pricing */
.areas{top:1809px;left:0;width:1200px;height:331px;background:var(--light)}
.areas h2{left:149px;top:95px;font-size:28px;font-weight:500;color:#222}
.area{position:absolute;display:flex;gap:8px;align-items:flex-start}
.area b{display:block;font-weight:400;font-size:14px;color:#333;line-height:16px}
.area small{display:block;font-size:10px;color:var(--orange)}
.pricing{left:645px;top:66px;width:403px;height:210px}
.pricing ul{list-style:none;position:absolute;left:54px;top:89px;width:290px;font-size:10.5px;color:#fff;line-height:19.7px}
.pricing li{display:flex;align-items:center;gap:4px;white-space:nowrap}
.pricing li span.fill{flex:1;border-bottom:1px dashed rgba(255,255,255,.8);height:0;margin-top:2px}
.pricing .tab-title{position:absolute;left:62px;top:12px;width:279px;text-align:center;font-size:23px;font-weight:600;color:#fff}

/* feedback */
.feedback{top:2140px;left:0;width:1200px;height:380px;background:linear-gradient(180deg,#262626,#222)}
.feedback h2{left:0;width:1200px;top:42px;text-align:center;font-size:28px;font-weight:600;color:#fff}
.quote-mark{left:584px;top:92px;width:30px;height:30px;border:2px solid #fff;border-radius:50%;display:flex;align-items:center;justify-content:center;color:#fff;font-size:16px;font-weight:700}
.feedback blockquote{left:250px;top:133px;width:700px;text-align:center;font-size:11px;font-style:italic;line-height:19.5px;color:#aaa}
.feedback .by{left:0;width:1200px;top:218px;text-align:center;font-size:10px;color:#aaa;line-height:16px}
.feedback .by strong{display:block;color:#fff;font-weight:600;font-size:10px}
.avatars{left:548px;top:262px}

/* partners */
.partners{top:2520px;left:0;width:1200px;height:205px;background:#fff}
.partner{position:absolute;top:63px;width:124px;height:94px;border:1px solid #e6e6e6;display:flex;align-items:center;justify-content:center}
.partner i{display:block;width:62px;height:62px;border-radius:50%;background:#d4d4d4}
.partner i.sq{border-radius:4px;width:80px;height:40px}

/* footer */
.site-footer{top:2725px;left:0;width:1200px;height:288px;background:linear-gradient(180deg,#222,#1b1b1b)}
.site-footer .brand{left:148px;top:46px;font-size:34px}
.site-footer .about-txt{left:150px;top:100px;width:225px;font-size:10.5px;line-height:18px;color:#bbb}
.socials{left:150px;top:188px;display:flex;gap:7px}
.socials i{display:block;width:23px;height:23px;border:1.5px solid #ddd;border-radius:50%}
.site-footer h4{position:absolute;font-size:12.5px;font-weight:600;color:#fff;top:38px}
.links{left:424px;top:70px;list-style:none;font-size:10.5px;line-height:21px;color:#bbb}
.news{position:absolute;left:594px;display:flex;gap:12px}
.news .thumb{width:45px;height:40px;background:linear-gradient(135deg,#9aa4ad,#dfe3e6)}
.news p{font-size:10.5px;line-height:15px;color:#bbb;width:130px}
.news p em{font-style:normal;color:var(--orange);display:block}
.field{position:absolute;left:845px;width:206px;border:1px solid #444;background:#262626;font-size:9px;color:#bbb;padding:7px 6px}
.send{position:absolute;left:845px;top:216px;width:206px;height:27px;background:var(--orange);color:#fff;font-size:12px;font-weight:600;display:flex;align-items:center;justify-content:center}
.copyright{left:0;width:1200px;top:270px;text-align:center;font-size:8.5px;color:#bbb}
</style>
</head>
<body>

<header class="site-header">
  <div class="abs brand">Vanto Rim</div>
  <nav class="abs main-nav"><span>HOME</span><span>ABOUT US</span><span>SERVICES</span><span>PRICING</span><span>AREAS SERVED</span><span>CONTACT US</span></nav>
  <div class="abs phone-pill"><span class="ico"><svg width="9" height="9" viewBox="0 0 24 24"><path fill="#fff" d="M6.6 10.8a15 15 0 0 0 6.6 6.6l2.2-2.2c.3-.3.7-.4 1-.2 1.1.4 2.3.6 3.6.6.6 0 1 .4 1 1V20c0 .6-.4 1-1 1A17 17 0 0 1 3 4c0-.6.4-1 1-1h3.5c.6 0 1 .4 1 1 0 1.3.2 2.5.6 3.6.1.3 0 .7-.2 1z"/></svg></span>(800) 555 0142</div>
</header>

<section class="abs hero">
  <div class="abs" role="img" aria-label="Smiling technician in a hard hat holding a security camera beside a ladder" style="inset:0"></div>
  <h1 class="abs">TAKE CONTROL OF<br>YOUR HOME SECURITY</h1>
  <p class="abs">Lorem Ipsum is simply dummy text of the printing and typesetting industry. Lorem Ipsum has been the</p>
  <span class="abs btn">Book a service</span>
  <div class="abs dots"><i></i><i></i><i></i></div>
</section>

<section class="abs about">
  <h2 class="abs">About <span class="brand">Vanto Rim</span></h2>
  <div class="abs copy">
    <p>Lorem Ipsum is simply dummy text of the printing and typesetting industry. Lorem Ipsum has been the industry's standard dummy text ever since the 1500s, when an unknown printer took a galley of type and scrambled it to make a type specimen book. It has survived not only five centuries, but also the leap into electronic typesetting, remaining essentially unchanged.</p>
    <p>It was popularised in the 1960s with the release of Corvenna sheets containing Lorem Ipsum passages, and more recently with desktop publishing software like Tamrin LayoutPro including versions of Lorem Ipsum.</p>
  </div>
  <div class="abs about-img-a" role="img" aria-label="Hands typing on a laptop in orange tone"></div>
  <div class="abs about-img-b" role="img" aria-label="Hand holding a glowing network of connected home device icons"></div>
</section>

<section class="abs services">
  <h2 class="abs">Our Services</h2>
  <div class="card" style="left:150px;top:121px"><div class="pic" role="img" aria-label="Technician repairing an opened smartphone" style="background:linear-gradient(135deg,#cfd3d8,#5d6570)"></div><div class="label">Phone Repair<span class="go"><svg width="14" height="14" viewBox="0 0 14 14"><path d="M2 2l5 5-5 5M7 2l5 5-5 5" stroke="#fff" stroke-width="1.6" fill="none"/></svg></span></div></div>
  <div class="card" style="left:453px;top:121px"><div class="pic" role="img" aria-label="Two installers mounting a flat television" style="background:linear-gradient(135deg,#f1f1f1,#bfc3c8)"></div><div class="label">TV Mounting<span class="go"><svg width="14" height="14" viewBox="0 0 14 14"><path d="M2 2l5 5-5 5M7 2l5 5-5 5" stroke="#fff" stroke-width="1.6" fill="none"/></svg></span></div></div>
  <div class="card" style="left:756px;top:121px"><div class="pic" role="img" aria-label="Hands holding a white dome security camera" style="background:linear-gradient(135deg,#e9e9e9,#a7a7a7)"></div><div class="label">Security Camera Installation<span class="go"><svg width="14" height="14" viewBox="0 0 14 14"><path d="M2 2l5 5-5 5M7 2l5 5-5 5" stroke="#fff" stroke-width="1.6" fill="none"/></svg></span></div></div>
  <div class="card" style="left:150px;top:354px"><div class="pic" role="img" aria-label="Hand plugging a cable into a network switch" style="background:linear-gradient(135deg,#2b2b2b,#a89a90)"></div><div class="label">Networking / Wi-Fi<span class="go"><svg width="14" height="14" viewBox="0 0 14 14"><path d="M2 2l5 5-5 5M7 2l5 5-5 5" stroke="#fff" stroke-width="1.6" fill="none"/></svg></span></div></div>
  <div class="card" style="left:453px;top:354px"><div class="pic" role="img" aria-label="Hand holding a phone with a smart home app" style="background:linear-gradient(135deg,#8c8a86,#3d6fa3)"></div><div class="label">Smart Home Services<span class="go"><svg width="14" height="14" viewBox="0 0 14 14"><path d="M2 2l5 5-5 5M7 2l5 5-5 5" stroke="#fff" stroke-width="1.6" fill="none"/></svg></span></div></div>
  <div class="card" style="left:756px;top:354px"><div class="pic" role="img" aria-label="Hand typing on a white keyboard" style="background:linear-gradient(135deg,#f4f4f4,#c9c9c9)"></div><div class="label">IT Support<span class="go"><svg width="14" height="14" viewBox="0 0 14 14"><path d="M2 2l5 5-5 5M7 2l5 5-5 5" stroke="#fff" stroke-width="1.6" fill="none"/></svg></span></div></div>
</section>

<section class="abs simple">
  <h2 class="abs">A simple way to take care of everything</h2>
  <p class="abs">Lorem Ipsum is simply dummy text of the printing and typesetting industry. Lorem Ipsum has been the industry's standard dummy text ever since the 1500s, when an unknown printer took a galley of type and scrambled it to make a type specimen book.</p>
  <span class="abs btn">Book a service</span>
  <div class="abs photo" role="img" aria-label="Family relaxing together on a sofa by a bright window"></div>
</section>

<section class="abs areas">
  <h2 class="abs">Areas Served</h2>
  <div class="area" style="left:150px;top:155px"><svg width="11" height="15" viewBox="0 0 11 15"><path d="M5.5 0A5.5 5.5 0 0 0 0 5.5C0 9.6 5.5 15 5.5 15S11 9.6 11 5.5A5.5 5.5 0 0 0 5.5 0zm0 7.7a2.2 2.2 0 1 1 0-4.4 2.2 2.2 0 0 1 0 4.4z" fill="#333"/></svg><div><b>Toronto</b><small>View map</small></div></div>
  <div class="area" style="left:255px;top:155px"><svg width="11" height="15" viewBox="0 0 11 15"><path d="M5.5 0A5.5 5.5 0 0 0 0 5.5C0 9.6 5.5 15 5.5 15S11 9.6 11 5.5A5.5 5.5 0 0 0 5.5 0zm0 7.7a2.2 2.2 0 1 1 0-4.4 2.2 2.2 0 0 1 0 4.4z" fill="#333"/></svg><div><b>Toronto</b><small>View map</small></div></div>
  <div class="area" style="left:360px;top:155px"><svg width="11" height="15" viewBox="0 0 11 15"><path d="M5.5 0A5.5 5.5 0 0 0 0 5.5C0 9.6 5.5 15 5.5 15S11 9.6 11 5.5A5.5 5.5 0 0 0 5.5 0zm0 7.7a2.2 2.2 0 1 1 0-4.4 2.2 2.2 0 0 1 0 4.4z" fill="#333"/></svg><div><b>Toronto</b><small>View map</small></div></div>
  <div class="area" style="left:150px;top:213px"><svg width="11" height="15" viewBox="0 0 11 15"><path d="M5.5 0A5.5 5.5 0 0 0 0 5.5C0 9.6 5.5 15 5.5 15S11 9.6 11 5.5A5.5 5.5 0 0 0 5.5 0zm0 7.7a2.2 2.2 0 1 1 0-4.4 2.2 2.2 0 0 1 0 4.4z" fill="#333"/></svg><div><b>Toronto</b><small>View map</small></div></div>
  <div class="area" style="left:255px;top:213px"><svg width="11" height="15" viewBox="0 0 11 15"><path d="M5.5 0A5.5 5.5 0 0 0 0 5.5C0 9.6 5.5 15 5.5 15S11 9.6 11 5.5A5.5 5.5 0 0 0 5.5 0zm0 7.7a2.2 2.2 0 1 1 0-4.4 2.2 2.2 0 0 1 0 4.4z" fill="#333"/></svg><div><b>Toronto</b><small>View map</small></div></div>
  <div class="area" style="left:360px;top:213px"><svg width="11" height="15" viewBox="0 0 11 15"><path d="M5.5 0A5.5 5.5 0 0 0 0 5.5C0 9.6 5.5 15 5.5 15S11 9.6 11 5.5A5.5 5.5 0 0 0 5.5 0zm0 7.7a2.2 2.2 0 1 1 0-4.4 2.2 2.2 0 0 1 0 4.4z" fill="#333"/></svg><div><b>Toronto</b><small>View map</small></div></div>

  <div class="abs pricing">
    <svg class="abs" style="left:0;top:0" width="403" height="210" viewBox="0 0 403 210">
      <defs><linearGradient id="priceGrad" x1="0" x2="1"><stop offset="0" stop-color="#1a5ff0"/><stop offset="1" stop-color="#22c0f3"/></linearGradient></defs>
      <path d="M57 4h8v14h-8zM338 4h8v14h-8z" fill="#1e3fa8"/>
      <path d="M8 22 Q0 22 4 34 L38 196 Q40 208 52 208 H352 Q364 208 366 196 L400 34 Q404 22 396 22 Z" fill="url(#priceGrad)"/>
      <path d="M62 0 H341 V50 Q341 54 337 54 H66 Q62 54 62 50 Z" fill="#f7931e"/>
      <path d="M62 50 H341 V56 H62z" fill="#d97a0c" opacity=".6"/>
    </svg>
    <div class="tab-title">PRICING</div>
    <ul>
      <li>Phone Repair<span class="fill"></span>$20.00</li>
      <li>TV Mounting<span class="fill"></span>$20.00</li>
      <li>Security Camera Installation<span class="fill"></span>$20.00</li>
      <li>Networking / Wi-Fi<span class="fill"></span>$20.00</li>
      <li>Smart Home Services<span class="fill"></span>$20.00</li>
      <li>IT Support<span class="fill"></span>$20.00</li>
    </ul>
  </div>
</section>

<section class="abs feedback">
  <h2 class="abs">Client Feedback</h2>
  <div class="abs quote-mark">“</div>
  <blockquote class="abs">Lorem Ipsum is simply dummy text of the printing and typesetting industry. Lorem Ipsum has been the industry's standard dummy text ever since the 1500s, when an unknown printer took a galley of type and scrambled it to make a type specimen book. standard dummy text ever since the 1500s, when an unknown printer took.</blockquote>
  <div class="abs by">by<strong>MARA DELTON</strong></div>
  <svg class="abs avatars" width="104" height="66" viewBox="0 0 104 66" role="img" aria-label="Row of client portrait thumbnails">
    <g stroke="#fff" stroke-width="2">
      <polygon points="16,1 30,9 30,25 16,33 2,25 2,9" fill="#8d8f92"/>
      <polygon points="50,1 64,9 64,25 50,33 36,25 36,9" fill="#6d6f72"/>
      <polygon points="84,1 98,9 98,25 84,33 70,25 70,9" fill="#a38b7c"/>
      <polygon points="33,31 47,39 47,55 33,63 19,55 19,39" fill="#9a8d86"/>
      <polygon points="67,31 81,39 81,55 67,63 53,55 53,39" fill="#b59886"/>
    </g>
  </svg>
</section>

<section class="abs partners" aria-label="Partner badges">
  <div class="partner" style="left:178px"><i></i></div>
  <div class="partner" style="left:324px"><i class="sq"></i></div>
  <div class="partner" style="left:470px"><i class="sq"></i></div>
  <div class="partner" style="left:616px"><i class="sq"></i></div>
  <div class="partner" style="left:762px"><i></i></div>
  <div class="partner" style="left:908px"><i></i></div>
</section>

<footer class="abs site-footer">
  <div class="abs brand">Vanto Rim</div>
  <p class="abs about-txt">Lorem Ipsum is simply dummy text of the printing and typesetting industry. Lorem Ipsum has been the industry's standard dummy text ever since the 1500s</p>
  <div class="abs socials"><i></i><i></i><i></i><i></i></div>

  <h4 style="left:422px">QUICK LINKS</h4>
  <ul class="abs links"><li>Home</li><li>About Us</li><li>Services</li><li>Pricing</li><li>Areas Served</li><li>Contact Us</li></ul>

  <h4 style="left:592px">LATEST NEWS</h4>
  <div class="news" style="top:70px"><div class="thumb" role="img" aria-label="News thumbnail"></div><p>Lorem Ipsum is simply dummy text of the<em>15 Dec, 2019</em></p></div>
  <div class="news" style="top:132px"><div class="thumb" role="img" aria-label="News thumbnail" style="background:linear-gradient(135deg,#b9e0e6,#eef6f7)"></div><p>Lorem Ipsum is simply dummy text of the<em>15 Dec, 2019</em></p></div>

  <h4 style="left:845px">GET IN TOUCH</h4>
  <div class="field" style="top:68px;height:28px">Name:</div>
  <div class="field" style="top:100px;height:28px">Email:</div>
  <div class="field" style="top:132px;height:58px">Email:</div>
  <div class="send">SEND</div>

  <div class="abs copyright">© 2020 VANTO RIM &nbsp;ALL RIGHTS RESERVED.</div>
</footer>

</body>
</html>
```